Display Layouts per segment use-cases

21.5in portrait (9:16) x 2
Office towers
Hotels
Shopping Malls

Target Market(s)

Office towers / Hotels / Shopping Malls

```html
<!DOCTYPE html>
<html lang="en">
<head>
<meta charset="UTF-8">
<title>NORVA — Lobby Display</title>
<link href="https://fonts.googleapis.com/css2?family=Montserrat:wght@700;800&family=Outfit:wght@300;400;500;600&display=swap" rel="stylesheet">
<style>
  :root {
    --sky-top: #2a8fd6;
    --sky-mid: #5db3e6;
    --glass-deep: #2f6f8a;
    --glass-light: #8fc7d8;
    --street: #c9c2b8;
    --street-dark: #3a3d42;
    --panel-top: rgba(16, 104, 196, 0.92);
    --panel-bottom: rgba(40, 140, 225, 0.88);
    --accent-strip: rgba(64, 205, 205, 0.78);
    --teal: #2cbfc3;
    --teal-dark: #3aa6a6;
    --white: #ffffff;
  }
  * { margin: 0; padding: 0; box-sizing: border-box; }
  html, body { width: 675px; height: 1200px; overflow: hidden; background: #fff; }
  .display {
    position: relative;
    width: 675px;
    height: 1200px;
    overflow: hidden;
    font-family: "Outfit", sans-serif;
    color: var(--white);
  }
  .scene-photo {
    position: absolute;
    inset: 0;
    background:
      linear-gradient(180deg,
        var(--sky-top) 0%,
        var(--sky-mid) 12%,
        var(--glass-light) 22%,
        var(--glass-deep) 45%,
        var(--glass-light) 60%,
        var(--glass-deep) 72%,
        #6a7f86 78%,
        var(--street) 84%,
        #b9b1a6 92%,
        var(--street-dark) 100%);
  }
  .info-panel {
    position: absolute;
    left: 0; top: 0;
    width: 247px; height: 1200px;
    background: linear-gradient(90deg, var(--panel-top) 0%, var(--panel-bottom) 100%);
  }
  .accent-strip {
    position: absolute;
    left: 247px; top: 0;
    width: 34px; height: 1200px;
    background: var(--accent-strip);
  }
  .brand-name {
    position: absolute;
    left: 19px; top: 72px;
    width: 205px;
    font-family: "Montserrat", sans-serif;
    font-weight: 800;
    font-size: 50px;
    letter-spacing: -1.5px;
    line-height: 1;
    white-space: nowrap;
  }
  .weather-icon {
    position: absolute;
    left: 24px; top: 322px;
    width: 170px; height: 125px;
    overflow: visible;
  }
  .temperature {
    position: absolute;
    left: 30px; top: 452px;
    font-weight: 500;
    font-size: 88px;
    line-height: 1;
    letter-spacing: -3px;
  }
  .temperature .unit-degree { font-weight: 400; font-size: 70px; vertical-align: 28px; letter-spacing: 0; }
  .temperature .unit-scale { font-weight: 300; font-size: 58px; letter-spacing: 0; margin-left: 4px; }
  .clock {
    position: absolute;
    left: 27px; top: 632px;
    font-weight: 600;
    font-size: 56px;
    line-height: 1;
    letter-spacing: -2px;
  }
  .clock .meridiem { font-weight: 300; font-size: 26px; vertical-align: 24px; letter-spacing: 0; margin-left: 6px; }
  .divider {
    position: absolute;
    left: 30px; top: 696px;
    width: 173px; height: 1px;
    background: var(--white);
  }
  .weekday {
    position: absolute;
    left: 29px; top: 706px;
    font-weight: 300;
    font-size: 22px;
    line-height: 1;
  }
  .date {
    position: absolute;
    left: 28px; top: 733px;
    font-weight: 600;
    font-size: 34px;
    line-height: 1;
    letter-spacing: -0.5px;
    white-space: nowrap;
  }
  .direction-badge {
    position: absolute;
    left: 298px; top: 870px;
    width: 315px; height: 315px;
  }
</style>
</head>
<body>
<main class="display">
  <div class="scene-photo" role="img" aria-label="Photo of a mirrored-glass office tower with palm trees reflected in its facade, blue sky with clouds, and a street corner in front"></div>

  <section class="info-panel">
    <h1 class="brand-name">NORVA</h1>

    <svg class="weather-icon" viewBox="0 0 170 125" aria-label="Partly cloudy">
      <g stroke="#fff" stroke-width="4" stroke-linecap="round">
        <line x1="54" y1="3" x2="54" y2="15"/>
        <line x1="25" y1="14" x2="32" y2="21"/>
        <line x1="83" y1="14" x2="76" y2="21"/>
        <line x1="8" y1="44" x2="20" y2="44"/>
        <line x1="25" y1="74" x2="32" y2="67"/>
      </g>
      <circle cx="54" cy="44" r="22" fill="#fff"/>
      <path d="M34 120 H140 A22 22 0 0 0 140 76 A36 36 0 0 0 72 60 A24 24 0 0 0 40 82 A19 19 0 0 0 34 120 Z"
            fill="#fff" stroke="#1f78cc" stroke-width="4"/>
    </svg>

    <p class="temperature">26<span class="unit-degree">°</span><span class="unit-scale">C</span></p>
    <p class="clock">07:15<span class="meridiem">PM</span></p>
    <div class="divider"></div>
    <p class="weekday">MONDAY</p>
    <p class="date">15 AUGUST</p>
  </section>

  <div class="accent-strip"></div>

  <svg class="direction-badge" viewBox="0 0 315 315" aria-label="Direction: straight ahead, 5">
    <circle cx="157" cy="160" r="152" fill="#2cbfc3"/>
    <circle cx="154" cy="156" r="146" fill="#fff"/>
    <polygon points="154,28 154,146 78,186" fill="#2cbfc3"/>
    <polygon points="154,28 230,186 154,146" fill="#3aa6a6"/>
    <text x="154" y="275" text-anchor="middle" font-family="Outfit, sans-serif" font-weight="500" font-size="118" fill="#2cbfc3">5</text>
  </svg>
</main>
</body>
</html>
```